Bright Meadow Counseling Business Card design with a visually interesting use of Space

I need business cards that are luxurious and give a peaceful, calm vibe. I also had some letterhead designed, and i like the look of it also, it's attached with the logo design for reference/ ideas but feel free to be creative.

Target Market(s)

High end luxurious client who needs counseling

Industry/Entity Type

Marriage and Family Therapy

Contact Information for Business Card

Mira Kowalczyk MS LMFT/ or Toby Hallett address 4150 Larkin Suite 600

Font styles to use
Sans Serif

Colors
0054AA
0677BA
7BADD7
CADEEF
E8F1F8
0094D4
00A9DD
6FCCEA
C7EBF8
E9F6FB
A7469A
B969AE
D3A5CF
EDDBEB
F8F0F9
6B429C
8869AF
B7A5CE
E3DAEB
F3F0F8

Requirements
Must have
• Logo and color scheme but be simple modern and luxurious
Nice to have
• I'd like to incorporate some elelmets from the logo and letterhead into a simple modern card

```html
<!DOCTYPE html>
<html lang="en">
<head>
<meta charset="utf-8">
<title>Bright Meadow Counseling – Business Card</title>
<link rel="stylesheet" href="https://fonts.googleapis.com/css2?family=Poppins:wght@300;500&display=swap">
<style>
  :root {
    --backdrop: #d6d6d6;
    --paper: #ffffff;
    --ink: #2a2a2a;
    --magenta: #A7469A;
    --violet: #6B429C;
    --sky: #7BADD7;
    --teal: #1fb0b0;
    --soft-blue: #6FCCEA;
  }
  * { box-sizing: border-box; margin: 0; padding: 0; }
  html, body {
    width: 1200px; height: 800px; overflow: hidden;
    background: var(--backdrop);
    font-family: "Poppins", sans-serif;
  }
  .sheet {
    width: 1200px; height: 800px;
    display: flex; align-items: center; justify-content: center; gap: 40px;
  }
  .card {
    position: relative;
    width: 560px; height: 320px;
    background: var(--paper);
    box-shadow: 0 10px 28px rgba(0,0,0,0.18);
    overflow: hidden;
  }
  .brand {
    position: absolute;
    display: flex; align-items: center; gap: 14px;
  }
  .brand-name {
    font-weight: 300; color: var(--ink);
    font-size: 30px; line-height: 1.1; letter-spacing: 0.5px;
  }
  .brand-dot {
    width: 34px; height: 34px; border-radius: 50%;
    background: var(--violet);
  }
  .card--front .brand { left: 150px; top: 48px; }
  .card--back .brand { left: 150px; top: 96px; }

  .therapists {
    position: absolute; right: 40px; top: 148px;
    text-align: right; color: var(--magenta);
    font-weight: 500; font-size: 15px; line-height: 1.5;
  }
  .therapists .or { color: var(--sky); }
  .edge-tab {
    position: absolute; right: 0; top: 176px;
    width: 9px; height: 30px; background: var(--violet);
    border-radius: 3px 0 0 3px;
  }
  .divider {
    position: absolute; left: 36px; top: 222px;
    width: 450px; height: 2px;
    background: linear-gradient(to right,
      var(--violet) 0 26%, var(--sky) 26% 53%, var(--teal) 53% 100%);
  }
  .contact {
    position: absolute; left: 36px; top: 236px;
    list-style: none; font-size: 12.5px; color: var(--magenta);
    line-height: 1.55;
  }
  .contact li { display: flex; align-items: center; gap: 8px; }
  .contact svg { width: 12px; height: 12px; fill: var(--teal); }
  .location {
    position: absolute; right: 74px; top: 240px;
    text-align: right; font-size: 14px; font-weight: 500; line-height: 1.5;
  }
  .location .address { color: var(--magenta); }
  .location .web { color: var(--violet); }
  .card--back .web {
    position: absolute; left: 150px; top: 196px;
    font-size: 13px; font-weight: 500; color: var(--violet);
  }
</style>
</head>
<body>
<main class="sheet">
  <section class="card card--front" aria-label="Business card front">
    <div class="brand">
      <p class="brand-name">Bright Meadow<br>Counseling</p>
      <span class="brand-dot"></span>
    </div>
    <p class="therapists">Mira Kowalczyk MS LMFT <span class="or">or</span><br>Toby Hallett</p>
    <span class="edge-tab"></span>
    <div class="divider"></div>
    <ul class="contact">
      <li>
        <svg viewBox="0 0 24 24" aria-hidden="true"><path d="M6.6 10.8a15.1 15.1 0 0 0 6.6 6.6l2.2-2.2a1 1 0 0 1 1-.25 11.4 11.4 0 0 0 3.6.57 1 1 0 0 1 1 1V20a1 1 0 0 1-1 1A17 17 0 0 1 3 4a1 1 0 0 1 1-1h3.5a1 1 0 0 1 1 1c0 1.25.2 2.45.57 3.6a1 1 0 0 1-.25 1z"/></svg>
        555-014-2873
      </li>
      <li>
        <svg viewBox="0 0 24 24" aria-hidden="true"><path d="M6 3h12v5H6zM3 9h18a1 1 0 0 1 1 1v7h-4v4H6v-4H2v-7a1 1 0 0 1 1-1zm5 7v3h8v-3z"/></svg>
        555-014-6120
      </li>
      <li>
        <svg viewBox="0 0 24 24" aria-hidden="true"><path d="M2 5h20v14H2zm2 2v.5l8 5 8-5V7l-8 5z"/></svg>
        hello@brightmeadow.com
      </li>
    </ul>
    <div class="location">
      <p class="address">4150 Larkin Suite 600</p>
      <p class="web">www.brightmeadow.com</p>
    </div>
  </section>

  <section class="card card--back" aria-label="Business card back">
    <div class="brand">
      <p class="brand-name">Bright Meadow<br>Counseling</p>
      <span class="brand-dot"></span>
    </div>
    <p class="web">www.brightmeadow.com</p>
  </section>
</main>
</body>
</html>
```